P.K.Harbor Services Business Card

We need a bi-lingual card (spanish/english). Information should be name, hours, services and address/phone. I am including a flyer as a reference--much of the information is included on it (spanish/english as well). THE COMPANY IS CALLED "P.K. HARBOR SERVICES" AND WE THINK THAT "P.K." SHOULD SUFFICE AS A LOGO--BUT WE DON'T HAVE THAT FONT NAILED DOWN. Colors should be Green/Blue scale. Happy colors. It's a check cashing business.

```html
<!DOCTYPE html>
<html lang="en">
<head>
<meta charset="utf-8">
<title>P.K. Harbor Services – Business Card</title>
<link rel="stylesheet" href="https://fonts.googleapis.com/css2?family=Baloo+2:wght@700;800&family=Montserrat:wght@500;600&display=swap">
<style>
  :root {
    --backdrop: #a7a7a7;
    --card: #ffffff;
    --navy: #1f3682;
    --sky: #29b6f0;
    --red: #e1190f;
    --yellow: #fff200;
    --light: #ffffff;
  }
  * { margin: 0; padding: 0; box-sizing: border-box; }
  html, body { width: 1200px; height: 436px; overflow: hidden; }
  body {
    background: var(--backdrop);
    position: relative;
    font-family: "Montserrat", sans-serif;
  }
  .card {
    position: absolute;
    width: 452px;
    height: 258px;
    background: var(--card);
    overflow: hidden;
  }
  .card--front { left: 106px; top: 83px; }
  .card--back { left: 657px; top: 79px; }

  .accent-bar { position: absolute; }
  .accent-bar--top {
    left: 0; top: 0; width: 314px; height: 4px;
    background: var(--sky);
    clip-path: polygon(0 0, 100% 0, 99% 100%, 0 100%);
  }
  .accent-bar--bottom {
    right: 0; bottom: 0; width: 240px; height: 5px;
    background: var(--navy);
    clip-path: polygon(2% 0, 100% 0, 100% 100%, 0 100%);
  }

  .brand-name {
    font-family: "Baloo 2", sans-serif;
    font-weight: 800;
    color: var(--navy);
    white-space: nowrap;
    letter-spacing: 0.2px;
    line-height: 1;
  }
  .card--front .brand-name {
    position: absolute;
    left: 0; right: 0; top: 107px;
    text-align: center;
    font-size: 37px;
  }
  .card--back .brand-name {
    position: absolute;
    left: 23px; top: 24px;
    font-size: 24px;
  }

  .side-panel { position: absolute; inset: 0; width: 100%; height: 100%; }

  .service-title {
    position: absolute;
    left: 18px; top: 124px;
    font-family: "Baloo 2", sans-serif;
    font-weight: 800;
    font-size: 30px;
    line-height: 1;
    color: var(--red);
    white-space: nowrap;
  }
  .service-points {
    position: absolute;
    left: 20px; top: 160px;
    list-style: none;
    font-family: "Baloo 2", sans-serif;
    font-weight: 800;
    font-size: 15px;
    line-height: 17px;
    color: var(--navy);
    white-space: nowrap;
  }
  .language-pill {
    position: absolute;
    left: 17px; top: 200px;
    width: 138px; height: 22px;
    border-radius: 11px;
    background: var(--yellow);
    color: var(--red);
    font-family: "Baloo 2", sans-serif;
    font-weight: 800;
    font-size: 12px;
    line-height: 23px;
    text-align: center;
    white-space: nowrap;
  }

  .contact-list { position: absolute; left: 300px; top: 0; list-style: none; }
  .contact-item {
    position: absolute;
    left: 0;
    display: flex;
    align-items: center;
    gap: 7px;
    color: var(--light);
    white-space: nowrap;
    font-weight: 600;
  }
  .contact-item svg { width: 24px; height: 24px; flex: none; }
  .contact-item--address { top: 67px; font-size: 9.5px; line-height: 12.5px; }
  .contact-item--phone { top: 116px; font-size: 9.5px; }
  .contact-item--hours { top: 162px; font-size: 8.5px; line-height: 11px; }
</style>
</head>
<body>

<section class="card card--front">
  <div class="accent-bar accent-bar--top"></div>
  <h1 class="brand-name">P.K. HARBOR SERVICES</h1>
  <div class="accent-bar accent-bar--bottom"></div>
</section>

<section class="card card--back">
  <svg class="side-panel" viewBox="0 0 452 258" aria-hidden="true">
    <polygon points="310,0 236,161 305,258 452,258 452,0" fill="var(--red)"/>
    <polygon points="314,0 245,161 316,258 452,258 452,0" fill="var(--navy)"/>
  </svg>

  <h2 class="brand-name">P.K. HARBOR SERVICES</h2>

  <p class="service-title">CHECK CA$HING</p>
  <ul class="service-points">
    <li>ALL CHECKS WELCOME!</li>
    <li>BEST RATES IN RIVERBEND</li>
  </ul>
  <p class="language-pill">¡SE HABLA ESPAÑOL!</p>

  <ul class="contact-list">
    <li class="contact-item contact-item--address">
      <svg viewBox="0 0 24 24" aria-hidden="true">
        <circle cx="12" cy="12" r="11" fill="none" stroke="var(--light)" stroke-width="1"/>
        <path d="M12 6.5a3.3 3.3 0 0 0-3.3 3.3c0 2.4 3.3 6.2 3.3 6.2s3.3-3.8 3.3-6.2A3.3 3.3 0 0 0 12 6.5z" fill="var(--light)"/>
        <circle cx="12" cy="9.8" r="1.2" fill="var(--navy)"/>
      </svg>
      <span>48 LINDEN AVENUE<br>MAPLE RIDGE, NY</span>
    </li>
    <li class="contact-item contact-item--phone">
      <svg viewBox="0 0 24 24" aria-hidden="true">
        <circle cx="12" cy="12" r="11" fill="none" stroke="var(--light)" stroke-width="1"/>
        <path d="M8.6 7c.4-.3.9-.2 1.1.2l1 1.8c.2.4.1.8-.2 1.1l-.7.6c.6 1.3 1.5 2.3 2.8 2.9l.6-.7c.3-.3.7-.4 1.1-.2l1.8 1c.4.2.5.7.2 1.1l-.8 1c-.4.5-1.1.6-1.7.4-2.9-1.1-5-3.3-6-6.1-.2-.6 0-1.3.4-1.7z" fill="var(--light)"/>
      </svg>
      <span>(555) 214 - 3090</span>
    </li>
    <li class="contact-item contact-item--hours">
      <svg viewBox="0 0 24 24" aria-hidden="true">
        <circle cx="12" cy="12" r="11" fill="none" stroke="var(--light)" stroke-width="1"/>
        <circle cx="12" cy="12" r="4.6" fill="none" stroke="var(--light)" stroke-width="1.6"/>
        <path d="M12 9.6V12h-1.8" fill="none" stroke="var(--light)" stroke-width="1.3" stroke-linecap="round"/>
      </svg>
      <span>MONDAY-SATURDAY<br>9AM-9PM</span>
    </li>
  </ul>
</section>

</body>
</html>
```